Redo my diagrams for print in a Magazine - files attached - ASAP

Hi, I have 3 diagrams that I have done that are dodgy, that I need to look good. They need to be high quality to be printed in a magazine for an article I am writing. And of course I need them yesterday. Actually I need them in 8 hours.

If there was a A4 version that could be downloaded, that would be excellent.

Cheers

Rob

Target Market(s)

Medial Magazine article

Industry/Entity Type

Medical

Font styles to use
Sans Serif

Requirements
Must have
• Must be able to be printed, in a magazine.
Nice to have
• Nice to have an A4 downloadable version

```html
<!DOCTYPE html>
<html lang="en">
<head>
<meta charset="utf-8">
<title>What people with no pain have on their knee MRIs</title>
<link href="https://fonts.googleapis.com/css2?family=Montserrat:wght@400;500;600;800&display=swap" rel="stylesheet">
<style>
  :root {
    --navy: #50628c;
    --steel: #7d8fb5;
    --paper: #fdfdfd;
    --page: #ffffff;
    --ink: #1f1f1f;
    --white: #ffffff;
  }
  * { margin: 0; padding: 0; box-sizing: border-box; }
  html, body {
    width: 1200px; height: 1200px; overflow: hidden;
    background: var(--page);
    font-family: "Montserrat", sans-serif;
  }
  .canvas { position: relative; width: 1200px; height: 1200px; }
  .poster {
    position: absolute; left: 191px; top: 21px;
    width: 743px; height: 1052px;
    background: var(--paper);
    transform: scale(1.1); transform-origin: top left;
    overflow: hidden;
  }
  .shapes { position: absolute; inset: 0; }
  .title {
    position: absolute; left: 0; top: 26px; width: 610px;
    text-align: center; color: var(--white);
    font-weight: 800; font-size: 31px; line-height: 40px;
  }
  .stat {
    position: absolute; height: 58px; width: 235px;
    display: flex; flex-direction: column; justify-content: center;
    color: var(--white); font-weight: 500; font-size: 16px; line-height: 22px;
    letter-spacing: 0.2px;
  }
  .stat--left { left: 0; padding-left: 22px; }
  .stat--right { left: 508px; padding-right: 24px; text-align: right; }
  .scan {
    position: absolute; left: 243px; top: 314px; width: 252px; height: 344px;
    background: radial-gradient(ellipse at 50% 50%, #3a3a3a 0%, #232323 55%, #161616 100%);
  }
  .note {
    position: absolute; left: 517px; top: 544px; width: 214px; height: 114px;
    display: flex; flex-direction: column; justify-content: center; gap: 14px;
    text-align: center; color: var(--ink); font-size: 11.5px; line-height: 14px;
    letter-spacing: 0.3px;
  }
  .headline {
    position: absolute; left: 173px; top: 728px; width: 391px; height: 58px;
    display: flex; align-items: center; justify-content: center;
    color: var(--white); font-weight: 500; font-size: 39px; letter-spacing: 0.5px;
  }
  .tagline {
    position: absolute; left: 0; top: 808px; width: 714px; text-align: center;
    color: var(--navy); font-weight: 500; font-size: 23px; letter-spacing: 0.3px;
  }
  .references {
    position: absolute; left: 35px; top: 959px; width: 685px;
    color: var(--white); font-weight: 600; font-size: 7.6px; line-height: 10px;
  }
  .references p + p { margin-top: 12px; }
</style>
</head>
<body>
<div class="canvas">
  <article class="poster">
    <svg class="shapes" width="743" height="1052" viewBox="0 0 743 1052" aria-hidden="true">
      <!-- header -->
      <polygon points="680,0 743,0 743,75 617,75" fill="var(--steel)"/>
      <polygon points="0,0 680,0 572,125 0,125" fill="var(--navy)"/>
      <!-- left stat tabs -->
      <polygon points="0,236 228,236 200,294 0,294" fill="var(--navy)"/>
      <polygon points="0,406 228,406 200,464 0,464" fill="var(--navy)"/>
      <polygon points="0,603 228,603 200,661 0,661" fill="var(--navy)"/>
      <!-- right stat tabs -->
      <polygon points="508,236 743,236 743,294 536,294" fill="var(--navy)"/>
      <polygon points="508,314 743,314 743,372 536,372" fill="var(--navy)"/>
      <polygon points="508,388 743,388 743,446 536,446" fill="var(--navy)"/>
      <polygon points="508,462 743,462 743,520 536,520" fill="var(--navy)"/>
      <!-- note brackets -->
      <g fill="none" stroke="var(--ink)" stroke-width="2">
        <polyline points="517,562 517,544 545,544"/>
        <polyline points="703,544 731,544 731,562"/>
        <polyline points="517,640 517,658 545,658"/>
        <polyline points="703,658 731,658 731,640"/>
      </g>
      <!-- headline tab -->
      <polygon points="173,728 564,728 536,786 201,786" fill="var(--navy)"/>
      <!-- footer -->
      <polygon points="169,892 743,892 743,920 122,920" fill="var(--steel)"/>
      <rect x="0" y="920" width="743" height="132" fill="var(--navy)"/>
    </svg>

    <h1 class="title">What people with no pain have<br>on their knee MRI’s</h1>

    <div class="stat stat--left" style="top:236px">88% have at least<br>1 abnormality (1)</div>
    <div class="stat stat--left" style="top:406px">72% have<br>osteophytes (1)</div>
    <div class="stat stat--left" style="top:603px">Bone marow lesions<br>are seen in 50%(1)</div>

    <div class="stat stat--right" style="top:236px">68% have cartilage<br>damage (1)</div>
    <div class="stat stat--right" style="top:314px">36% have<br>synovitis(1)</div>
    <div class="stat stat--right" style="top:388px">9% have torn<br>ligaments (1)</div>
    <div class="stat stat--right" style="top:462px">25% have<br>maniscal tears(1)</div>

    <div class="scan" role="img" aria-label="Coronal knee MRI scan, greyscale"></div>

    <div class="note">
      <p>But in people over 50,<br>-60% of people with NO PAIN<br>have mensical tears</p>
      <p>-And 63% of people WITH PAIN<br>have mensical tears (2)</p>
    </div>

    <div class="headline">0% have pain</div>
    <p class="tagline">Just because its on the scan doesn’t mean it hurts</p>

    <footer class="references">
      <p>1. Marlowe A, Tarn J, Okada D, Velde FW, Lindqvist M, Rao T, et al. Prevalence of abnormalities in knees detected by MRI in adults without knee osteoarthritis: population based observational study (Brookvale Osteoarthritis Study). NMJ. Northfield Medical Press; 2012;345:e5339.</p>
      <p>2. Lindqvist M, Marlowe A, Hale D, Fisher DJ, Karimi P, Doyle M, et al. Incidental mensical findings on knee MRI in middle-age and elderly persons. Clin Joint Rev. 2008 Sep 11;359(11):1108-15</p>
    </footer>
  </article>
</div>
</body>
</html>
```